Label Design Refresh for existing High End Supplement line

Design a label for our high end supplement brand, packaged in a Cobal Blue bottle.... using Clear labels as the label stock media.

A clear label design will take advantage of the blue bottle and can incorporate any design element you create, metalic elements, new graphics etc.

our line spans 50 different product categories and over 400 unique SKUs, so any elements you suggest to differentiate products or categories will be appreciated.

see: www.quillantheralife.com
Updates

Need designers to meet project requirements. Full label, clear label stock design (clear background with exception for design elements and text etc.)

Target Market(s)

Men and Women 25-55 Health conscious and not price sensitive. Product is 5x higher cost than competition.

Industry/Entity Type

Sexual health for men and women. testosterone, hormone health, nootropics

Font styles to use
Sans Serif

Colors

Designer to choose colors to be used in the design.

Requirements
Must have
• Clear label design for Cobalt blue, packer style, pharma bottle. Must feature Velmora brand on front panel. Must show entire label panel design as 2.8in x 7.25in. Graphics can be full color with metalic or foil type elements.
Nice to have
• Name of products include: SHBG, Testosterone & Libido, Adrenal Support Phase 2, LH Formula, ADHD Phase1,
Should not have
• Busy designs that are stock images for supplement label layouts

```html
<!DOCTYPE html>
<html lang="en">
<head>
<meta charset="utf-8">
<title>Velmora Supplement Label</title>
<link href="https://fonts.googleapis.com/css2?family=Rajdhani:wght@500;700&family=Bebas+Neue&display=swap" rel="stylesheet">
<style>
  :root {
    --label-blue: #1c43d6;
    --panel-blue: #1a3cc4;
    --orange: #f07c1b;
    --green: #8cc63f;
    --leaf-green: #6fb832;
    --white: #ffffff;
    --grey: #e3e3e3;
    --page: #ffffff;
  }
  * { box-sizing: border-box; margin: 0; padding: 0; }
  html, body { width: 1200px; height: 927px; overflow: hidden; background: var(--page); }
  body { position: relative; font-family: "Rajdhani", sans-serif; color: var(--white); }

  .label-sheet {
    position: absolute; left: 100px; top: 60px;
    width: 1000px; height: 386px;
    background: var(--label-blue); border-radius: 22px; overflow: hidden;
  }
  .leaf-corner {
    position: absolute; left: 0; top: 0; width: 70px; height: 60px;
    background: linear-gradient(135deg, var(--green), var(--leaf-green));
    border-bottom-right-radius: 60px;
  }
  .leaf-edge {
    position: absolute; right: 0; top: 222px; width: 12px; height: 80px;
    background: linear-gradient(180deg, var(--green), var(--leaf-green));
    border-radius: 12px 0 0 12px;
  }
  .rule-orange { position: absolute; height: 3px; background: var(--orange); }
  .copy-lines { position: absolute; left: 72px; top: 90px; width: 252px; }
  .copy-lines span { display: block; height: 4px; background: var(--white); margin-bottom: 6px; }
  .info-box { position: absolute; left: 72px; top: 267px; width: 254px; height: 51px; background: var(--grey); }
  .symbol-row { position: absolute; left: 68px; top: 338px; }

  .front-panel {
    position: absolute; width: 316px; height: 386px; text-align: center;
  }
  .label-sheet .front-panel { left: 336px; top: 0; background: var(--panel-blue); }
  .brand-mark {
    position: absolute; left: 50%; top: 27px; width: 106px; height: 106px;
    margin-left: -53px; border-radius: 50%; background: var(--orange);
  }
  .brand-name {
    position: absolute; left: 0; right: 0; top: 142px;
    font-weight: 700; font-size: 50px; letter-spacing: 1px; line-height: 1;
  }
  .product-band { position: absolute; left: 0; top: 221px; width: 316px; height: 52px; }
  .band-line { position: absolute; left: 0; right: 0; height: 4px; }
  .band-line.white { background: var(--white); }
  .band-line.orange { background: var(--orange); }
  .product-oval {
    position: absolute; left: 50%; top: 0; width: 140px; height: 52px; margin-left: -70px;
    background: var(--green); border: 3px solid var(--panel-blue); border-radius: 50%;
    display: flex; align-items: center; justify-content: center;
    color: var(--panel-blue); font-weight: 500; line-height: 0.95;
  }
  .product-oval.single { font-size: 30px; }
  .product-oval.double { font-size: 14px; letter-spacing: 0.5px; }
  .capsule-count { position: absolute; left: 0; right: 0; top: 309px; font-size: 19px; font-weight: 500; letter-spacing: 0.5px; }
  .count-rule { position: absolute; left: 50%; top: 339px; width: 36px; margin-left: -18px; height: 3px; background: var(--orange); }
  .supplement-type { position: absolute; left: 0; right: 0; top: 345px; font-size: 16px; font-weight: 500; }

  .sprig-icon {
    position: absolute; left: 690px; top: 33px; width: 44px; height: 44px;
    background: radial-gradient(circle, var(--green), var(--leaf-green)); border-radius: 50%;
  }
  .facts-title {
    position: absolute; left: 743px; top: 38px;
    font-family: "Bebas Neue", sans-serif; font-size: 33px; letter-spacing: 0.5px; line-height: 1;
  }
  .facts-table { position: absolute; left: 745px; top: 77px; width: 150px; height: 206px; border: 2px solid var(--white); padding: 14px 8px 0; }
  .facts-table span { display: block; height: 2px; background: var(--white); margin-bottom: 15px; }
  .dot-row { position: absolute; left: 745px; top: 322px; display: flex; gap: 9px; }
  .dot-row span { width: 10px; height: 10px; border-radius: 50%; background: var(--white); }
  .site-url { position: absolute; left: 818px; top: 318px; font-size: 12px; font-weight: 500; letter-spacing: 0.3px; }

  .range-row { position: absolute; left: 40px; top: 500px; width: 1121px; height: 251px; }
  .range-item { position: absolute; top: 0; width: 205px; height: 251px; overflow: hidden; border-radius: 14px; background: var(--panel-blue); }
  .range-item .front-panel { left: 0; top: 0; transform: scale(0.65); transform-origin: 0 0; }
</style>
</head>
<body>

<section class="label-sheet" aria-label="Full label, 2.8 by 7.25 inches">
  <div class="leaf-corner" role="img" aria-label="Green leaf sprig decoration"></div>
  <div class="rule-orange" style="left:72px; top:40px; width:248px;"></div>
  <div class="copy-lines" aria-hidden="true">
    <span></span><span></span><span></span><span></span><span></span><span></span>
    <span></span><span></span><span></span><span></span><span></span><span></span><span></span>
  </div>
  <div class="info-box"></div>
  <svg class="symbol-row" width="260" height="32" viewBox="0 0 260 32">
    <polygon points="15,2 28,28 2,28" fill="none" stroke="#fff" stroke-width="2"/>
    <rect x="47" y="9" width="42" height="12" fill="#fff"/>
    <circle cx="122" cy="16" r="14" fill="#fff"/>
  </svg>

  <div class="front-panel">
    <div class="brand-mark"></div>
    <div class="brand-name">VELMORA</div>
    <div class="product-band">
      <div class="band-line white" style="top:3px"></div>
      <div class="band-line orange" style="top:16px"></div>
      <div class="band-line orange" style="top:30px"></div>
      <div class="band-line white" style="top:44px"></div>
      <div class="product-oval single">SHBG</div>
    </div>
    <div class="capsule-count">60 VEGETABLE CAPSULES</div>
    <div class="count-rule"></div>
    <div class="supplement-type">Dietary Supplement</div>
  </div>

  <div class="sprig-icon" role="img" aria-label="Small green leaf sprig icon"></div>
  <div class="facts-title">NUTRITION FACTS</div>
  <div class="facts-table" aria-hidden="true">
    <span></span><span></span><span></span><span></span><span></span><span></span>
    <span></span><span></span><span></span><span></span><span></span>
  </div>
  <div class="dot-row"><span></span><span></span><span></span><span></span></div>
  <div class="site-url">www.quillantheralife.com</div>
  <div class="rule-orange" style="left:675px; top:338px; width:308px;"></div>
  <div class="leaf-edge" role="img" aria-label="Green leaf decoration at label edge"></div>
</section>

<section class="range-row" aria-label="Product range front panels">
  <div class="range-item" style="left:0">
    <div class="front-panel">
      <div class="brand-mark"></div><div class="brand-name">VELMORA</div>
      <div class="product-band">
        <div class="band-line white" style="top:3px"></div><div class="band-line orange" style="top:16px"></div>
        <div class="band-line orange" style="top:30px"></div><div class="band-line white" style="top:44px"></div>
        <div class="product-oval single">SHBG</div>
      </div>
      <div class="capsule-count">60 VEGETABLE CAPSULES</div><div class="count-rule"></div>
      <div class="supplement-type">Dietary Supplement</div>
    </div>
  </div>
  <div class="range-item" style="left:229px">
    <div class="front-panel">
      <div class="brand-mark"></div><div class="brand-name">VELMORA</div>
      <div class="product-band">
        <div class="band-line white" style="top:3px"></div><div class="band-line orange" style="top:16px"></div>
        <div class="band-line orange" style="top:30px"></div><div class="band-line white" style="top:44px"></div>
        <div class="product-oval double">TESTOSTERONE<br>&amp; LIBIDO</div>
      </div>
      <div class="capsule-count">60 VEGETABLE CAPSULES</div><div class="count-rule"></div>
      <div class="supplement-type">Dietary Supplement</div>
    </div>
  </div>
  <div class="range-item" style="left:458px">
    <div class="front-panel">
      <div class="brand-mark"></div><div class="brand-name">VELMORA</div>
      <div class="product-band">
        <div class="band-line white" style="top:3px"></div><div class="band-line orange" style="top:16px"></div>
        <div class="band-line orange" style="top:30px"></div><div class="band-line white" style="top:44px"></div>
        <div class="product-oval double">ADRENAL SUPPORT<br>PHASE 2</div>
      </div>
      <div class="capsule-count">60 VEGETABLE CAPSULES</div><div class="count-rule"></div>
      <div class="supplement-type">Dietary Supplement</div>
    </div>
  </div>
  <div class="range-item" style="left:687px">
    <div class="front-panel">
      <div class="brand-mark"></div><div class="brand-name">VELMORA</div>
      <div class="product-band">
        <div class="band-line white" style="top:3px"></div><div class="band-line orange" style="top:16px"></div>
        <div class="band-line orange" style="top:30px"></div><div class="band-line white" style="top:44px"></div>
        <div class="product-oval double">LH FORMULA</div>
      </div>
      <div class="capsule-count">60 VEGETABLE CAPSULES</div><div class="count-rule"></div>
      <div class="supplement-type">Dietary Supplement</div>
    </div>
  </div>
  <div class="range-item" style="left:916px">
    <div class="front-panel">
      <div class="brand-mark"></div><div class="brand-name">VELMORA</div>
      <div class="product-band">
        <div class="band-line white" style="top:3px"></div><div class="band-line orange" style="top:16px"></div>
        <div class="band-line orange" style="top:30px"></div><div class="band-line white" style="top:44px"></div>
        <div class="product-oval double">ADHD<br>PHASE 1</div>
      </div>
      <div class="capsule-count">60 VEGETABLE CAPSULES</div><div class="count-rule"></div>
      <div class="supplement-type">Dietary Supplement</div>
    </div>
  </div>
</section>

</body>
</html>
```